dentist office tri-fold for root canal specialist

design a tri fold brochure to give to patients talking about the office and the services
Talk about doctors and their bios
services: root canal , retreatments, endodontic surgery, trauma, cracked teeth
Technology: CBCT, microscopes, lasers, clear pulse advanced
I will provide all the technical info. willing to hire a writer if needed. Attached a picture of our logo as a reference of our colors. Can attach older versions of brochure if requested. Looking for a very professional tri fold that will be used to market the practice to patients and other doctors.
Rough idea: TRIFOLD
Front Cover:
Welcome to The Halvern Team
Thank you for allowing us to care for your endodontic needs. We look forward to serving you.
We at The Halvern Team have dedicated our professional lives to improving the comfort and dental health of those in our care.
Inner Right:
Pics of Docs
Welcome – On behalf of our staff, we welcome you to our office.
We are pleased that you have selected our team of professionals to care for your endodontic needs. We want you to know that we are committed to providing you, our patient with the highest quality endodontic care in the most gentle, efficient, and caring manner possible. We pride ourselves on offering our expertise along with the best patient care with the most up to date technologies to better ensure your oral health.
For your convenience, please visit us online at www.thehalvernteam.com for directions to our offices, pre and post-operative instructions, general information on our Endodontists and much more. We are here for you and our doctors are on call 24 hours a day, 7 days a week.
We are looking forward providing you a most relaxed and pleasant vist possible. Thank you again for choosing The Halvern Team.
Inner Middle:
What is a Root Canal?
A root canal (endodontic treatment) is one of the most common dental procedures performed, with more than 14 million performed every year. This simple treatment can save your natural teeth and prevent the need of dental implants or bridges.
At the center of your tooth is pulp. The pulp is a collection of blood vessels, nerves and lymphatics, which help to form the tooth during the stages of tooth development.
I’ve already had a root canal, why do I need another procedure?
Retreatment - A second chance to save your tooth
With proper care, most teeth which have had endodontic (root canal) treatment can last as long as other natural teeth.
However, in a few cases, a tooth that has received endodontic treatment fails to heal completely. And occasionally, a tooth becomes painful or diseased months or even years after previously successful endodontic treatment.
If your tooth has failed to heal or has developed new problems, you have a second chance. Another endodontic procedure, called retreatment, may be able to save your tooth.
Retreated teeth can function well for years, even for a lifetime. It's always best to save the tooth if your endodontist believes retreatment is the best option for you.
Advances in technology are constantly changing the way root canal treatment is performed, so your endodontist may even be able to use a new technique that was not available when you had your first procedure.
Of course, there are no guarantees with any dental or medical procedure. Your endodontist will discuss your options and the chances of success before beginning retreatment.
What is an Apicoectomy?
In this procedure, the endodontist opens the gum tissue near the tooth to see the underlying bone and to remove any inflamed or infected tissue. The very end of the root is also removed or resected.
Inner Right:
Patient Care: Needing a root canal is often a surprise and sometimes an emergency. We at The Halvern Team make certain that every patient receives prompt emergency care at any time.
We understand how uneasy some patients may feel about dental visits and how we can make a difference in providing a relaxing, positive experience. Our doctors are trained in different levels of sedation dentistry from Nitrous Oxide to Conscious Sedation.
Our entire team is dedicated to providing you with excellent, personalized care and service to make your visit as comfortable and pleasant as possible. You will enjoy our relaxing treatment rooms, complete with plumacore coverings, televisions and Tunelets for your use during treatment and blankets to keep you warm if you’re cold.
Technical Equipment: The Halvern Team prides itself in utilizing the most advanced techniques and state-of-the-art equipment including digital radiography, fiber optic illumination, ultrasonic equipment, and operating microscopes, which help the doctor see microscopic details inside a tooth during micro-surgical and non-surgical procedures.
Expertise: The Halvern Team is staffed by doctors who are responsive to your concerns and alert to your experience during treatment. All of our doctors are endodontists, which means they are specialists who have completed 2-3 years of advanced training in addition to dental school. We are all specialist members of the Continental Society of Pulp Specialists (CSPS). All our endodontists continue their education and training through professional associations, seminars, study groups, and teaching both at Pellmoor and Dorrin Universities.

```html
<!DOCTYPE html>
<html lang="en">
<head>
<meta charset="utf-8">
<title>The Halvern Team – Tri-fold Brochure</title>
<link href="https://fonts.googleapis.com/css2?family=Open+Sans:ital,wght@0,400;0,600;0,700;0,800;1,400;1,600;1,700&display=swap" rel="stylesheet">
<style>
  :root{
    --navy:#25308c;
    --navy-deep:#1c2474;
    --mid-blue:#5d70c8;
    --sky:#7c8fda;
    --pale:#eef0f7;
    --paper:#ffffff;
    --ink:#2c2f3a;
    --grey:#6a6d78;
    --backdrop:#d3dbdb;
  }
  *{box-sizing:border-box;margin:0;padding:0}
  html,body{width:1200px;height:1200px;overflow:hidden}
  body{background:var(--backdrop);font-family:"Open Sans",Arial,sans-serif;color:var(--ink);position:relative}
  .spread{position:absolute;left:30px;width:1140px;height:555px;display:flex;box-shadow:0 6px 18px rgba(0,0,0,.18)}
  .spread--outside{top:25px}
  .spread--inside{top:620px}
  .panel{position:relative;width:380px;height:100%;background:linear-gradient(180deg,#fff 0%,#f6f7fb 100%);overflow:hidden}
  .panel + .panel{border-left:1px solid #e3e5ee}
  .photo{position:absolute;left:0;width:100%}
  .abs{position:absolute}
  .wave{position:absolute;left:0;width:100%}

  /* Outside left */
  .equip-photo{top:0;height:150px;background:linear-gradient(135deg,#3f9f8f 0%,#6fb5a8 35%,#b89a74 70%,#8a6a4b 100%)}
  .body-copy{font-size:11px;line-height:1.42;color:var(--ink)}
  .label{font-size:11.5px;font-weight:700;font-style:italic;color:var(--navy)}
  .outside-left .copy{top:170px;left:26px;right:24px}
  .outside-left .copy p{margin-bottom:10px}

  .band{position:absolute;left:0;width:100%;bottom:0;background:var(--navy);color:#fff}

  /* Outside middle */
  .intro{top:22px;left:30px;right:30px;text-align:center;font-size:10.5px;font-style:italic;line-height:1.4;color:var(--ink)}
  .practice-title{top:86px;left:0;right:0;text-align:center;font-size:18px;font-weight:700;font-style:italic;color:var(--navy);letter-spacing:.5px}
  .pin{top:118px;left:176px;width:28px;height:28px}
  .address{top:152px;left:0;right:0;text-align:center;font-size:12.5px;font-style:italic;color:var(--grey);line-height:1.5}
  .call{top:200px;left:0;right:0;text-align:center;font-size:20px;font-style:italic;font-weight:600;color:var(--navy)}
  .offer{left:28px;right:20px}
  .offer h3{font-size:13px;font-weight:700;font-style:italic;color:var(--navy);text-decoration:underline;margin-bottom:3px}
  .offer p{font-size:11.5px;font-style:italic;color:var(--ink);line-height:1.45}
  .offer--services{top:365px}
  .offer--tech{top:430px}
  .web-band{height:42px;background:var(--sky);display:flex;align-items:center;justify-content:center;font-size:15px;font-style:italic;font-weight:600;letter-spacing:.4px}

  /* Cover */
  .cover-head{top:0;left:0;width:100%;height:130px}
  .cover-title{top:18px;left:0;right:0;text-align:center;color:#fff}
  .cover-title .small{display:block;font-size:24px;font-weight:400;letter-spacing:1px}
  .cover-title .big{display:block;font-size:21px;font-weight:800;letter-spacing:2px;text-transform:uppercase}
  .patient-photo{top:120px;height:230px;background:linear-gradient(120deg,#7786d8 0%,#c8cfee 30%,#f0d7cd 55%,#e7b9a8 80%,#b6c2ea 100%)}
  .brand{top:368px;left:0;right:0;display:flex;align-items:center;justify-content:center;gap:10px;color:var(--navy);font-size:25px;font-weight:400;letter-spacing:1px}
  .brand .dot{width:22px;height:22px;border-radius:50%;background:var(--navy)}
  .thanks{top:418px;left:20px;right:20px;text-align:center;font-size:15.5px;font-weight:700;color:var(--navy);line-height:1.35}
  .cover-band{height:58px;display:flex;align-items:center;justify-content:center;font-size:19px;letter-spacing:.5px}

  /* Inside left */
  .top-rule{top:0;left:30px;width:230px;height:8px;background:var(--mid-blue)}
  .welcome-head{top:22px;left:28px;right:24px;font-size:12.5px;font-weight:700;font-style:italic;color:var(--navy);text-transform:uppercase;line-height:1.3}
  .welcome-copy{top:64px;left:28px;right:24px}
  .welcome-copy p{margin-bottom:8px}
  .on-call{top:330px;left:28px;width:140px;font-size:13px;font-weight:700;color:var(--navy);text-transform:uppercase;line-height:1.55;letter-spacing:1px}
  .doctor-photo{top:318px;left:175px;width:205px;height:197px;background:linear-gradient(180deg,#d8dce6 0%,#f4f4f6 45%,#e9edf4 100%)}
  .thanks-band{height:38px;display:flex;align-items:center;padding-left:24px;font-size:12px;font-weight:600}

  /* Inside middle */
  .rootcanal{top:20px;left:26px;right:22px;font-size:10.3px;font-style:italic;line-height:1.36}
  .rootcanal h2{font-size:16px;font-weight:700;color:var(--navy);margin-bottom:5px}
  .rootcanal p{margin-bottom:6px}
  .rootcanal .question{color:var(--mid-blue);margin-bottom:0}
  .rootcanal .sub{color:var(--navy);font-weight:700;margin-bottom:0}

  /* Inside right */
  .office-photo{top:0;height:62px;background:linear-gradient(90deg,#b5c3c9 0%,#e0e6e8 50%,#9fb0b8 100%)}
  .treatment-photo{bottom:0;height:115px;background:linear-gradient(120deg,#3d5a9a 0%,#8898b8 35%,#d4b8a6 65%,#a57e6a 100%)}
  .care{top:74px;left:24px;right:20px;font-size:10.6px;line-height:1.38}
  .care h2{font-size:17px;font-weight:700;color:var(--navy);margin-bottom:4px}
  .care p{margin-bottom:7px}
  .care .label{font-size:10.6px;font-style:normal}
</style>
</head>
<body>

<!-- Outside of the brochure -->
<section class="spread spread--outside">

  <article class="panel outside-left">
    <div class="photo equip-photo" role="img" aria-label="Photo of endodontists in scrubs working in a treatment room"></div>
    <svg class="wave" style="top:110px" width="380" height="60" viewBox="0 0 380 60" preserveAspectRatio="none">
      <path d="M0 22 C120 60 240 -5 380 30 L380 60 L0 60 Z" fill="#fff"/>
      <path d="M0 22 C120 60 240 -5 380 30" fill="none" stroke="var(--navy)" stroke-width="4"/>
    </svg>
    <div class="abs copy body-copy">
      <p><span class="label">Technical Equipment:</span><br>The Halvern Team prides itself in utilizing the most advanced techniques and state-of-the-art equipment including digital radiography, fiber optic illumination, ultrasonic equipment, and operating microscopes, which help the doctor see microscopic details inside a tooth during micro-surgical and non-surgical procedures.</p>
      <p><span class="label">Expertise:</span><br>The Halvern Team is staffed by doctors who are responsive to your concerns and alert to your experience during treatment. All of our doctors are endodontists, which means they are specialists who have completed 2-3 years of advanced training in addition to dental school. We are all specialist members of the Continental Society of Pulp Specialists (CSPS). All our endodontists continue their education and training through professional associations, seminars, study groups, and teaching both at Pellmoor and Dorrin Universities.</p>
    </div>
    <svg class="wave" style="bottom:0" width="380" height="50" viewBox="0 0 380 50" preserveAspectRatio="none">
      <path d="M0 14 L380 30 L380 50 L0 50 Z" fill="var(--navy)"/>
    </svg>
  </article>

  <article class="panel outside-middle">
    <p class="abs intro">We at The Halvern Team have dedicated our professional lives to improving the comfort and dental health of those in our care.</p>
    <h2 class="abs practice-title">THE HALVERN TEAM</h2>
    <svg class="abs pin" viewBox="0 0 28 28"><circle cx="14" cy="14" r="13" fill="var(--navy)"/><path d="M14 6.5a5 5 0 0 0-5 5c0 3.8 5 9 5 9s5-5.2 5-9a5 5 0 0 0-5-5z" fill="#fff"/><circle cx="14" cy="11.5" r="1.9" fill="var(--navy)"/></svg>
    <p class="abs address">Brightwater<br>Lake County, Northland</p>
    <p class="abs call">CALL US : (555) 014-2290</p>
    <svg class="wave" style="top:250px" width="380" height="110" viewBox="0 0 380 110" preserveAspectRatio="none">
      <path d="M0 95 C110 95 170 30 380 20" fill="none" stroke="var(--navy)" stroke-width="6"/>
      <path d="M0 104 C120 104 190 45 380 38" fill="none" stroke="var(--sky)" stroke-width="2"/>
    </svg>
    <div class="abs offer offer--services">
      <h3>Services</h3>
      <p>Root Canal, Retreatments, Endodontic Surgery, Trauma, Cracked Teeth</p>
    </div>
    <div class="abs offer offer--tech">
      <h3>Technology</h3>
      <p>CBCT, Microscopes, Lasers, Clear Pulse Advanced</p>
    </div>
    <div class="band web-band">www.thehalvernteam.com</div>
  </article>

  <article class="panel cover">
    <svg class="abs cover-head" width="380" height="130" viewBox="0 0 380 130" preserveAspectRatio="none">
      <path d="M0 0 H380 V118 C270 70 120 110 0 70 Z" fill="var(--navy)"/>
      <path d="M0 80 C120 120 270 80 380 128" fill="none" stroke="var(--mid-blue)" stroke-width="3"/>
    </svg>
    <h1 class="abs cover-title"><span class="small">Welcome to The</span><span class="big">Halvern Team</span></h1>
    <div class="photo patient-photo" role="img" aria-label="Photo of a smiling patient during a dental exam"></div>
    <svg class="wave" style="top:300px" width="380" height="60" viewBox="0 0 380 60" preserveAspectRatio="none">
      <path d="M0 50 C120 0 250 70 380 20 L380 60 L0 60 Z" fill="#fff"/>
      <path d="M0 50 C120 0 250 70 380 20" fill="none" stroke="var(--navy)" stroke-width="5"/>
    </svg>
    <div class="abs brand"><span class="dot"></span>The Halvern Team</div>
    <p class="abs thanks">Thank you for allowing us to care for your endodontic needs.</p>
    <div class="band cover-band">We look forward to serving you.</div>
  </article>
</section>

<!-- Inside of the brochure -->
<section class="spread spread--inside">

  <article class="panel inside-left">
    <div class="abs top-rule"></div>
    <h2 class="abs welcome-head">Welcome - On behalf of our staff we welcome you to our office</h2>
    <div class="abs welcome-copy body-copy">
      <p>We are pleased that you have selected our team of professionals to care for your endodontic needs. We want you to know that we are committed to providing you, our patient with the highest quality endodontic care in the most gentle, efficient, and caring manner possible. We pride ourselves on offering our expertise along with the best patient care with the most up to date technologies to better ensure your oral health.</p>
      <p>For your convenience, please visit us online at www.thehalvernteam.com for directions to our offices, pre and post-operative instructions, general information on our Endodontists and much more. We are looking forward providing you a most relaxed and pleasant visit possible.</p>
    </div>
    <p class="abs on-call">We are here for you and our doctors are on call 24 hours a day, 7 days a week.</p>
    <div class="photo doctor-photo" role="img" aria-label="Portrait photo of a doctor in a white coat"></div>
    <div class="band thanks-band">Thank you again for choosing The Halvern Team.</div>
  </article>

  <article class="panel inside-middle">
    <div class="abs rootcanal">
      <h2>What is a Root Canal?</h2>
      <p>A root canal (endodontic treatment) is one of the most common dental procedures performed, with more than 14 million performed every year. This simple treatment can save your natural teeth and prevent the need of dental implants or bridges.</p>
      <p>At the center of your tooth is pulp. The pulp is a collection of blood vessels, nerves and lymphatics, which help to form the tooth during the stages of tooth development.</p>
      <p class="question">I've already had a root canal, why do I need another procedure?</p>
      <p class="sub">Retreatment</p>
      <p>A second chance to save your tooth. With proper care, most teeth which have had endodontic (root canal) treatment can last as long as other natural teeth.</p>
      <p>However, in a few cases, a tooth that has received endodontic treatment fails to heal completely. And occasionally, a tooth becomes painful or diseased months or even years after previously successful endodontic treatment.</p>
      <p>If your tooth has failed to heal or has developed new problems, you have a second chance. Another endodontic procedure, called retreatment, may be able to save your tooth.</p>
      <p>Retreated teeth can function well for years, even for a lifetime. It's always best to save the tooth if your endodontist believes retreatment is the best option for you.</p>
      <p>Advances in technology are constantly changing the way root canal treatment is performed, so your endodontist may even be able to use a new technique that was not available when you had your first procedure.</p>
      <p>Of course, there are no guarantees with any dental or medical procedure. Your endodontist will discuss your options and the chances of success before beginning retreatment.</p>
    </div>
  </article>

  <article class="panel inside-right">
    <div class="photo office-photo" role="img" aria-label="Photo of dental treatment room equipment"></div>
    <div class="abs care">
      <h2>What is an Apicoectomy?</h2>
      <p>In this procedure, the endodontist opens the gum tissue near the tooth to see the underlying bone and to remove any inflamed or infected tissue. The very end of the root is also removed or resected.</p>
      <p><span class="label">Patient Care:</span> Needing a root canal is often a surprise and sometimes an emergency. We at The Halvern Team make certain that every patient receives prompt emergency care at any time.</p>
      <p>We understand how uneasy some patients may feel about dental visits and how we can make a difference in providing a relaxing, positive experience. Our doctors are trained in different levels of sedation dentistry from Nitrous Oxide to Conscious Sedation.</p>
      <p>Our entire team is dedicated to providing you with excellent, personalized care and service to make your visit as comfortable and pleasant as possible. You will enjoy our relaxing treatment rooms, complete with plumacore coverings, televisions and Tunelets for your use during treatment and blankets to keep you warm if you're cold.</p>
    </div>
    <div class="photo treatment-photo" role="img" aria-label="Photo of a patient receiving endodontic treatment"></div>
  </article>
</section>

</body>
</html>
```